Kevmoor belly band - cardboard to wrap around a plain tin for Gift

We are packaging men's and ladies handkerchiefs into tins for Gifts. We need two belly band designs to wrap around a small tin which measures 140 x 100 x 43 depth. The band to measure approx 90 w x 330 long inclusive is 30mm lapover . The ladies design (white tin) to have a subtle floral background with the word .Kevmoor. only placed on front centre of tin. The men's (black tin) to have a masculine look with the logo .Kevmoor. (the word can be taken out of the oval logo. This to placed in centre on front of tin. Men's could have a tan or cream textured look??

Target Market(s)

30 to 80 year old market

Font styles to use
Other font styles liked:
• Mona lisa

Colors

Designer to choose colors to be used in the design.

Requirements
Must have
• Two different designs one for men's black tin and one for ladies white tin.
• Must have continuous design with logo in centre once wrapped around the tin.
• Both must have an upmarket classy look.
• Tins will be displayed horizontal.
Nice to have
• Ladies would like to see soft floral not too over the top feminine classy look.
• Mens more masculine and upmarket maybe plain with a textured look.
• A design has been attached - like this sort of look for ladies!

```html
<!DOCTYPE html>
<html lang="en">
<head>
<meta charset="utf-8">
<title>Kevmoor belly bands</title>
<link href="https://fonts.googleapis.com/css2?family=Bodoni+Moda:wght@500&display=swap" rel="stylesheet">
<style>
  :root {
    --paper: #ffffff;
    --mark: #3a3a3a;
    --fold: #c8c8c8;
    --navy-deep: #34457a;
    --navy-light: #4c64a0;
    --blush-label: #f8eef4;
    --mauve-text: #b5708f;
    --tan-light: #ecc8ab;
    --tan-mid: #e1b08f;
    --tan-deep: #d9a17f;
    --label-black: #000000;
    --cream-text: #f7eadc;
  }
  html, body { margin: 0; padding: 0; overflow: hidden; }
  body { width: 1200px; height: 728px; background: var(--paper); }
  .sheet { position: relative; width: 1200px; height: 728px; }
  .band { position: absolute; left: 74px; width: 1056px; }
  .band--ladies {
    top: 70px; height: 286px;
    background:
      radial-gradient(circle at 20% 30%, rgba(231,163,198,.55), transparent 22%),
      radial-gradient(circle at 50% 70%, rgba(231,163,198,.5), transparent 24%),
      radial-gradient(circle at 80% 35%, rgba(231,163,198,.5), transparent 22%),
      linear-gradient(135deg, var(--navy-deep), var(--navy-light) 50%, var(--navy-deep));
  }
  .band--mens {
    top: 375px; height: 288px;
    background: linear-gradient(120deg, var(--tan-deep), var(--tan-light) 30%, var(--tan-mid) 55%, var(--tan-light) 75%, var(--tan-deep));
  }
  .fold-line { position: absolute; top: 52px; width: 0; height: 632px; border-left: 1px solid var(--fold); }
  .crop-mark { position: absolute; background: var(--mark); }
  .crop-mark--h { height: 1px; width: 22px; }
  .crop-mark--v { width: 1px; height: 22px; }
  .label {
    position: absolute; left: 134px; width: 191px; height: 116px;
    box-sizing: border-box; display: flex; flex-direction: column;
    align-items: center; justify-content: center;
    font-family: "Bodoni Moda", serif; font-weight: 500;
  }
  .label--ladies {
    top: 158px; background: var(--blush-label);
    border: 4px solid var(--blush-label); outline: 2px solid var(--paper); outline-offset: -8px;
    color: var(--mauve-text);
  }
  .label--mens {
    top: 462px; background: var(--label-black);
    box-shadow: inset 0 0 0 5px var(--label-black), inset 0 0 0 8px var(--tan-light);
    color: var(--cream-text);
  }
  .label__name { font-size: 34px; line-height: 1; letter-spacing: 1px; }
  .label__year { font-size: 13px; margin-top: 8px; letter-spacing: 2px; text-transform: uppercase; }
</style>
</head>
<body>
<div class="sheet">
  <div class="band band--ladies" role="img" aria-label="Soft floral pattern of pink and white roses with mauve leaves on a deep navy ground"></div>
  <div class="band band--mens" role="img" aria-label="Tan textured background with a faint embossed swirl pattern"></div>

  <div class="fold-line" style="left:384px"></div>
  <div class="fold-line" style="left:547px"></div>
  <div class="fold-line" style="left:859px"></div>
  <div class="fold-line" style="left:1017px"></div>

  <div class="crop-mark crop-mark--h" style="left:52px;top:69px"></div>
  <div class="crop-mark crop-mark--v" style="left:74px;top:47px"></div>
  <div class="crop-mark crop-mark--h" style="left:1130px;top:69px"></div>
  <div class="crop-mark crop-mark--v" style="left:1130px;top:47px"></div>
  <div class="crop-mark crop-mark--h" style="left:52px;top:662px"></div>
  <div class="crop-mark crop-mark--v" style="left:74px;top:662px"></div>
  <div class="crop-mark crop-mark--h" style="left:1130px;top:662px"></div>
  <div class="crop-mark crop-mark--v" style="left:1130px;top:662px"></div>

  <div class="label label--ladies">
    <div class="label__name">Kevmoor</div>
    <div class="label__year">Est. 1971</div>
  </div>
  <div class="label label--mens">
    <div class="label__name">Kevmoor</div>
    <div class="label__year">Est. 1971</div>
  </div>
</div>
</body>
</html>
```